Full Service Day Spa Needs Wordpress Template Designed

Verdant Spa is a full service day spa, where we make our own line of bath and body products. The current website houses an online store with an TradeNook base (as a WordPress plugin) and simple web pages with information and price lists for services.
For the upgraded website, we are doing a significant makeover and want to include the ability to have full screen video on our main page, windowed or full screen video on feature pages (for example, pages for "Meet our staff" or "Product Demos")
The site should retain standard WordPress compatibility for plugins, such as galleries etc.
The ability to include iframes would be considered a plus so that we can embed external scheduling applications that we subscribe to.
The color scheme for our spa features chocolate brown, taupe, cream, and turquoise for color accents. We would like our website to reflect these colors as our customers find them relaxing.
Our spa has a number of paintings on our walls, which could be used for inspiration for the website design. We like modern abstract art, with curves and swirls. I have included examples of this artwork so that potential designers can see what we like.
The new site must include our logo (provided) and our tag line: "Come Relax With Us" displayed in the upper left in the header.
We would prefer to have the option to put the menu either on the left side, or across the top to the right of the logo.
Words to describe the look we are seeking would be elegant, upscale, relaxing.

Target Market(s)

Our market is primarily local women (in and around our city) who are professionals aged 30 - 65.

Industry/Entity Type

Store

Colors
f78f20
00a990
f37022

Requirements
Must have
• The template should accommodate full screen and partial screen HTML5 video. Must have a menu, could be top or could be side. Should be in shades of browns and neutral colors, with teal accents, or similar highlights to the attached pictures of our artwork we have in the spa. We are looking for a consistent look that our customers can identify is us. Must have our logo in the upper left side of the header.
Nice to have
• Iframes built in would be nice, although we know we can get plugins for that. Likewise we know we can get plugins for the HTML 5 video, we would like the template built with accommodating that in mind. We have seen sites that have full screen video on the main page. We think this looks good.
Should not have
• We are looking for something elegant and upscale, so we are not looking for something "Cartoonish".

```html
<!DOCTYPE html>
<html lang="en">
<head>
<meta charset="utf-8">
<title>Verdant Spa – About Headaches</title>
<link rel="stylesheet" href="https://fonts.googleapis.com/css2?family=Cormorant+Garamond:wght@500&family=Oswald:wght@500&family=Arimo:wght@400;700&display=swap">
<style>
:root{
  --page:#f3f0ea;
  --chocolate:#3b2d22;
  --teal:#1e4a5a;
  --teal-dark:#163845;
  --brown-text:#6e3a2a;
  --body-text:#4a4440;
  --tan:#f8ebd7;
  --tan-border:#ecd9bb;
  --rust:#b4473b;
  --orange:#f46c2e;
  --accent:#e8552a;
  --white:#fff;
}
*{margin:0;padding:0;box-sizing:border-box}
html,body{width:921px;height:1200px;overflow:hidden;background:var(--page)}
body{position:relative;font-family:"Arimo",Arial,sans-serif;color:var(--body-text)}
.abs{position:absolute}

.brand{left:228px;top:8px;display:flex;align-items:center;gap:8px}
.brand-mark{width:34px;height:34px;border-radius:50%;background:#8b6a52}
.brand-name{font-family:"Cormorant Garamond",Georgia,serif;font-weight:500;font-size:30px;line-height:30px;color:var(--chocolate)}
.brand-tagline{font-family:"Cormorant Garamond",Georgia,serif;font-weight:500;font-size:12px;letter-spacing:.5px;color:var(--brown-text);text-transform:uppercase}

.slider{left:199px;top:64px;width:523px;height:202px;background:var(--chocolate)}
.slide-photo{position:absolute;left:0;top:23px;width:523px;height:179px;
  background:radial-gradient(ellipse at 40% 50%,#f7b25a 0%,#c7631d 35%,#4a1f0a 70%,#1a0d06 100%)}
.slide-arrow{position:absolute;top:94px;width:38px;height:38px}
.slide-arrow.prev{left:9px}.slide-arrow.next{left:469px}

.ribbon{left:137px;top:266px;width:625px;height:60px}
.main-nav{left:195px;top:266px;width:528px;height:42px;display:flex;align-items:center}
.main-nav a{position:absolute;top:10px;height:21px;line-height:21px;padding:0 11px;font-family:"Oswald",sans-serif;font-size:9px;color:var(--white);text-decoration:none;text-transform:uppercase}
.main-nav a.active{background:var(--teal-dark)}
.reserve{left:605px;top:308px;width:64px;height:25px;background:var(--rust);color:var(--white);font-family:"Oswald",sans-serif;font-size:9px;line-height:25px;text-align:center;text-transform:uppercase}

.section-title{font-family:"Cormorant Garamond",Georgia,serif;font-weight:500;font-size:13px;letter-spacing:.6px;color:var(--brown-text);text-transform:uppercase}
.about-head{left:198px;top:364px;width:344px;height:21px;border-bottom:1px solid #ddd6cc;display:flex;align-items:flex-start;gap:10px}
.share{width:16px;height:16px;border-radius:50%;margin-top:1px}
.share.one{background:#9fb1cf;margin-left:2px}.share.two{background:#8fcbe6;margin-left:-2px}
.article{left:198px;top:397px;width:344px}
.article p{font-size:7px;line-height:9.8px;text-align:justify;margin-bottom:12px}
.remedies-title{left:198px;top:656px}
.remedies{left:200px;top:680px;width:348px;height:67px;background:#1f1a12}
.thumb{position:absolute;top:15px;width:38px;height:38px;border:2px solid var(--white)}

.side-photo{top:350px;width:64px;height:62px}
.search{left:594px;top:423px;width:137px;height:20px;background:var(--white);border:1px solid #e1ddd6;font-size:7px;line-height:18px;padding-left:9px;color:#555}
.article-menu{left:594px;top:458px;width:137px}
.menu-row{height:20px;margin-bottom:2px;font-size:7px;line-height:20px;padding-left:9px;position:relative;background:var(--white);border:1px solid #eee6da}
.menu-row.head{background:var(--tan);border-color:var(--tan-border);font-weight:700;color:#333}
.menu-row.current{color:var(--accent);font-weight:700;padding-left:14px;border-left:4px solid var(--teal)}
.menu-row.more{background:var(--tan);border-color:var(--tan-border)}
.menu-row svg{position:absolute;right:9px;top:6px}

.tabs{left:593px;top:689px;width:138px;height:257px;background:#f3e3cd;border:1px solid var(--tan-border)}
.tab{position:absolute;top:6px;height:24px;font-family:"Oswald",sans-serif;font-size:7.5px;line-height:9px;text-align:center;text-transform:uppercase;color:#333;padding-top:3px}
.tab.active{background:var(--white)}
.tab-panel{position:absolute;left:5px;top:29px;width:127px;height:221px;background:var(--white)}
.post{position:absolute;left:10px;width:110px;height:41px;border-bottom:1px solid #eee}
.post-thumb{position:absolute;left:0;top:0;width:31px;height:31px}
.post-title{position:absolute;left:35px;top:1px;width:73px;font-size:7px;line-height:8px;font-weight:700;color:#333;text-align:justify}
.post-date{position:absolute;left:35px;top:22px;font-size:5.5px;color:#666}

.footer{left:198px;top:973px;width:532px;height:98px;background:var(--orange);color:var(--white);font-size:9.5px;text-align:center;padding-top:76px}
</style>
</head>
<body>

<header class="abs brand">
  <span class="brand-mark"></span>
  <div>
    <div class="brand-name">Verdant Spa</div>
    <div class="brand-tagline">Come relax with us</div>
  </div>
</header>

<section class="abs slider">
  <div class="slide-photo" role="img" aria-label="Close-up of rows of glowing tea-light candles"></div>
  <svg class="slide-arrow prev" viewBox="0 0 38 38"><circle cx="19" cy="19" r="18" fill="#fff" fill-opacity=".55" stroke="#fff" stroke-opacity=".7"/><path d="M9 19l17-9v18z" fill="#3a3a3a"/></svg>
  <svg class="slide-arrow next" viewBox="0 0 38 38"><circle cx="19" cy="19" r="18" fill="#fff" fill-opacity=".55" stroke="#fff" stroke-opacity=".7"/><path d="M29 19l-17-9v18z" fill="#3a3a3a"/></svg>
</section>

<svg class="abs ribbon" viewBox="0 0 625 60" aria-hidden="true">
  <defs><linearGradient id="shade" x1="0" y1="0" x2="0" y2="1"><stop offset="0" stop-color="#000" stop-opacity=".25"/><stop offset="1" stop-color="#000" stop-opacity="0"/></linearGradient></defs>
  <rect x="58" y="42" width="528" height="14" fill="url(#shade)"/>
  <path d="M0 14h58v43H0l14-21z" fill="#1e4a5a"/>
  <path d="M625 14h-57v43h57l-14-21z" fill="#1e4a5a"/>
  <path d="M58 42v15l20-15z" fill="#b08545"/>
  <path d="M586 42v15l-20-15z" fill="#b08545"/>
  <rect x="58" y="0" width="528" height="42" fill="#1e4a5a"/>
</svg>
<nav class="abs main-nav">
  <a style="left:57px">Home</a>
  <a class="active" style="left:112px">About</a>
  <a style="left:168px">Services</a>
  <a style="left:235px">Products</a>
  <a style="left:311px">Contact</a>
</nav>
<div class="abs reserve">Reservation</div>

<main>
  <div class="abs about-head">
    <h1 class="section-title">About&nbsp; Headaches</h1>
    <span class="share one"></span><span class="share two"></span>
  </div>
  <article class="abs article">
    <p>Lorem ipsum dolor sit amet, consectetur adipisicing elit, sed do eiusmod tempor incididunt ut labore et dolore magna aliqua. Ut enim ad minim veniam, quis nostrud exercitation ullamco laboris nisi ut aliquip ex ea commodo consequat. Duis aute irure dolor in reprehenderit in voluptate velit esse cillum dolore eu fugiat nulla pariatur. Excepteur sint occaecat cupidatat non proident, sunt in culpa qui officia deserunt mollit anim id est laborum.</p>
    <p>At vero eos et accusamus et iusto odio dignissimos ducimus qui blanditiis praesentium voluptatum deleniti atque corrupti quos dolores et quas molestias excepturi sint occaecati cupiditate non provident, similique sunt in culpa qui officia deserunt mollitia animi, id est laborum et dolorum fuga. Et harum quidem rerum facilis est et expedita distinctio. Nam libero tempore, cum soluta nobis est eligendi optio cumque nihil impedit quo minus id quod maxime placeat facere possimus, omnis voluptas assumenda est, omnis dolor repellendus.</p>
    <p>Lorem ipsum dolor sit amet, consectetur adipisicing elit, sed do eiusmod tempor incididunt ut labore et dolore magna aliqua. Ut enim ad minim veniam, quis nostrud exercitation ullamco laboris nisi ut aliquip ex ea commodo consequat. Duis aute irure dolor in reprehenderit in voluptate velit esse cillum dolore eu fugiat nulla pariatur. Excepteur sint occaecat cupidatat non proident, sunt in culpa qui officia deserunt mollit anim id est laborum.</p>
    <p>At vero eos et accusamus et iusto odio dignissimos ducimus qui blanditiis praesentium voluptatum deleniti atque corrupti quos dolores et quas molestias excepturi sint occaecati cupiditate non provident, similique sunt in culpa qui officia deserunt mollitia animi, id est laborum et dolorum fuga. Et harum quidem rerum facilis est et expedita distinctio. Nam libero tempore, cum soluta nobis est eligendi optio cumque nihil impedit quo minus id quod maxime placeat facere possimus, omnis voluptas assumenda est, omnis dolor repellendus.</p>
  </article>

  <h2 class="abs section-title remedies-title">Remedies to your headaches</h2>
  <div class="abs remedies">
    <div class="thumb" style="left:14px;background:linear-gradient(135deg,#c8502a,#6b3a1c)" role="img" aria-label="Flowers and spa stones"></div>
    <div class="thumb" style="left:60px;background:linear-gradient(135deg,#c9a23a,#4a3a12)" role="img" aria-label="Oil bottles"></div>
    <div class="thumb" style="left:106px;background:linear-gradient(135deg,#f0c23a,#a9762a)" role="img" aria-label="Yellow flowers"></div>
    <div class="thumb" style="left:152px;background:linear-gradient(135deg,#e8dccb,#b7713a)" role="img" aria-label="Jar of body scrub"></div>
    <div class="thumb" style="left:198px;background:linear-gradient(135deg,#8a74b0,#4a3560)" role="img" aria-label="Lavender and bottle"></div>
    <div class="thumb" style="left:244px;background:linear-gradient(135deg,#d9a43a,#3a4a1e)" role="img" aria-label="Essential oil bottle"></div>
    <div class="thumb" style="left:290px;background:linear-gradient(135deg,#9fcf4a,#2a5a1e)" role="img" aria-label="Green oil jar"></div>
  </div>
</main>

<aside>
  <div class="abs side-photo" style="left:591px;background:linear-gradient(135deg,#5b8a9a,#3a2a1e)" role="img" aria-label="Massage stones on wood"></div>
  <div class="abs side-photo" style="left:659px;background:linear-gradient(135deg,#e3a440,#6b4a2a)" role="img" aria-label="Candle and oils"></div>
  <div class="abs search">type and hit enter</div>

  <nav class="abs article-menu">
    <div class="menu-row head">Recent Articles<svg width="8" height="6" viewBox="0 0 8 6"><path d="M0 0h8L4 5z" fill="#333"/></svg></div>
    <div class="menu-row current">Lorem Ipsum Dolor</div>
    <div class="menu-row">Lorem Ipsum Dolor</div>
    <div class="menu-row">Lorem Ipsum Dolor</div>
    <div class="menu-row more">Testomonials<svg width="5" height="8" viewBox="0 0 5 8"><path d="M0 0l5 4-5 4z" fill="#333"/></svg></div>
    <div class="menu-row more">Sed ut Perspiciatis<svg width="5" height="8" viewBox="0 0 5 8"><path d="M0 0l5 4-5 4z" fill="#333"/></svg></div>
    <div class="menu-row more">Lorem Ipsum Dolor<svg width="5" height="8" viewBox="0 0 5 8"><path d="M0 0l5 4-5 4z" fill="#333"/></svg></div>
    <div class="menu-row more">Sed ut Perspiciatis<svg width="5" height="8" viewBox="0 0 5 8"><path d="M0 0l5 4-5 4z" fill="#333"/></svg></div>
    <div class="menu-row more">Lorem Ipsum Dolor<svg width="5" height="8" viewBox="0 0 5 8"><path d="M0 0l5 4-5 4z" fill="#333"/></svg></div>
    <div class="menu-row more">Sed ut Perspiciatis<svg width="5" height="8" viewBox="0 0 5 8"><path d="M0 0l5 4-5 4z" fill="#333"/></svg></div>
  </nav>

  <section class="abs tabs">
    <div class="tab active" style="left:5px;width:38px">Recent<br>Articles</div>
    <div class="tab" style="left:49px;width:40px">Popular<br>Articles</div>
    <div class="tab" style="left:91px;width:40px">Latest<br>Videos</div>
    <div class="tab-panel">
      <div class="post" style="top:15px"><div class="post-thumb" style="background:linear-gradient(#c9d3da,#6f7f88)" role="img" aria-label="Misty landscape"></div><div class="post-title">Duis aute irure dolor in reprehenderit</div><div class="post-date">Posted on 4th Dec, 2010</div></div>
      <div class="post" style="top:56px"><div class="post-thumb" style="background:linear-gradient(#d98a5a,#2a4a6a)" role="img" aria-label="Sunset over water"></div><div class="post-title">Nemo enim ipsam voluptatem</div><div class="post-date">Posted on 4th Dec, 2010</div></div>
      <div class="post" style="top:97px"><div class="post-thumb" style="background:linear-gradient(#b0305a,#2a1040)" role="img" aria-label="Colourful portrait artwork"></div><div class="post-title">Lorem ipsum dolor sit amet</div><div class="post-date">Posted on 4th Dec, 2010</div></div>
      <div class="post" style="top:138px"><div class="post-thumb" style="background:linear-gradient(#8a7aa0,#3a3040)" role="img" aria-label="Purple shoreline"></div><div class="post-title">Lorem ipsum dolor sit amet</div><div class="post-date">Posted on 4th Dec, 2010</div></div>
      <div class="post" style="top:179px;border:0"><div class="post-thumb" style="background:linear-gradient(#cfcfcf,#2a2a2a)" role="img" aria-label="Black and white nature scene"></div><div class="post-title">Lorem ipsum dolor sit amet</div><div class="post-date">Posted on 4th Dec, 2010</div></div>
    </div>
  </section>
</aside>

<footer class="abs footer">Terms of Use | Privacy Policy | Sitemap &nbsp;&nbsp;&nbsp;© Copyright 2014: Verdant Spa.</footer>

</body>
</html>
```